Three diagrams for an academic paper

I need professional-looking versions of three diagrams for an academic paper. I am uploading JPEGs of each diagram drafted in Vextra Docs. I need completely new versions that look much better.

Some detailed requirements:
- Professional styling - must be clearly superior to the ‘stick-figure’ example images and obviously not from powerpoint, etc.
- Must be a coordinated style across all three illustrations.
- Note that a mini-version of figure 2 appears in figure 3 (within the database image)
- I need very high resolution, suitable for a manuscript
- May need some text changes at short notice (anticipate 2 small updates to text)

Target Market(s)

Academics

Industry/Entity Type

Vextra

Font styles to use
Sans Serif

Colors

Designer to choose colors to be used in the design.

Requirements
Must have
• Don't look like powerpoint

```html
<!DOCTYPE html>
<html lang="en">
<head>
<meta charset="utf-8">
<title>Decreasing language, increasing structure</title>
<link rel="stylesheet" href="https://fonts.googleapis.com/css2?family=Roboto+Condensed:wght@400;700&display=swap">
<style>
  :root {
    --page: #ffffff;
    --ink: #111111;
    --panel-light: #4fa6ea;
    --panel-dark: #0a3d86;
    --sheet-light: #ffffff;
    --sheet-dark: #8c8f94;
    --sheet-edge: #2a2a2a;
    --rule: #1a1a1a;
    --swatch: #9ccaf5;
    --axis-light: #f4f5f6;
    --axis-dark: #7d8287;
  }
  html, body {
    margin: 0;
    padding: 0;
    width: 1200px;
    height: 406px;
    overflow: hidden;
    background: var(--page);
  }
  .figure {
    display: block;
    width: 1200px;
    height: 406px;
  }
  .stage-label {
    font-family: "Roboto Condensed", sans-serif;
    font-weight: 400;
    font-size: 19px;
    fill: var(--ink);
  }
  .axis-caption {
    font-family: "Roboto Condensed", sans-serif;
    font-weight: 700;
    font-size: 29px;
    fill: var(--ink);
  }
  .annotation-bits {
    font-family: "Roboto Condensed", sans-serif;
    font-weight: 700;
    font-size: 7.6px;
    fill: var(--ink);
  }
  .panel { fill: url(#panelFill); }
  .sheet { fill: url(#sheetFill); stroke: var(--sheet-edge); stroke-width: 1; }
  .sheet-rule { stroke: var(--rule); stroke-width: 1.3; }
  .swatch { fill: var(--swatch); stroke: #3d7fc4; stroke-width: 1; }
  .statement-bar { fill: url(#statementFill); stroke: var(--sheet-edge); stroke-width: 1; }
</style>
</head>
<body>
<svg class="figure" viewBox="0 0 1200 406" xmlns="http://www.w3.org/2000/svg">
  <defs>
    <linearGradient id="panelFill" x1="0" y1="0" x2="1" y2="1">
      <stop offset="0" stop-color="var(--panel-light)"/>
      <stop offset="0.55" stop-color="#2f82d4"/>
      <stop offset="1" stop-color="var(--panel-dark)"/>
    </linearGradient>
    <linearGradient id="sheetFill" x1="0" y1="0" x2="1" y2="0">
      <stop offset="0" stop-color="var(--sheet-dark)"/>
      <stop offset="0.45" stop-color="var(--sheet-light)"/>
      <stop offset="1" stop-color="#c9cbce"/>
    </linearGradient>
    <linearGradient id="statementFill" x1="0" y1="0" x2="1" y2="0">
      <stop offset="0" stop-color="#2d6fb8"/>
      <stop offset="0.5" stop-color="#7ab3e6"/>
      <stop offset="1" stop-color="#2d6fb8"/>
    </linearGradient>
    <linearGradient id="axisFill" x1="0" y1="0" x2="0" y2="1">
      <stop offset="0" stop-color="var(--axis-dark)"/>
      <stop offset="0.45" stop-color="var(--axis-light)"/>
      <stop offset="1" stop-color="var(--axis-dark)"/>
    </linearGradient>
    <g id="articleRules">
      <line class="sheet-rule" x1="10" y1="8" x2="58" y2="8"/>
      <line class="sheet-rule" x1="20" y1="17" x2="58" y2="17"/>
      <line class="sheet-rule" x1="14" y1="26" x2="58" y2="26"/>
      <line class="sheet-rule" x1="8" y1="35" x2="58" y2="35"/>
      <line class="sheet-rule" x1="18" y1="44" x2="58" y2="44"/>
      <line class="sheet-rule" x1="12" y1="53" x2="58" y2="53"/>
      <line class="sheet-rule" x1="22" y1="62" x2="58" y2="62"/>
      <line class="sheet-rule" x1="10" y1="71" x2="58" y2="71"/>
      <line class="sheet-rule" x1="16" y1="80" x2="58" y2="80"/>
      <line class="sheet-rule" x1="8" y1="89" x2="58" y2="89"/>
      <line class="sheet-rule" x1="20" y1="98" x2="58" y2="98"/>
      <line class="sheet-rule" x1="12" y1="107" x2="58" y2="107"/>
      <line class="sheet-rule" x1="18" y1="116" x2="58" y2="116"/>
      <line class="sheet-rule" x1="10" y1="125" x2="58" y2="125"/>
      <line class="sheet-rule" x1="22" y1="134" x2="58" y2="134"/>
      <line class="sheet-rule" x1="14" y1="143" x2="58" y2="143"/>
    </g>
  </defs>

  <!-- Stage 1: text article, no annotation -->
  <g class="stage">
    <text class="stage-label" x="70" y="70">A text article with</text>
    <text class="stage-label" x="70" y="96">no annotation data</text>
    <rect class="panel" x="70" y="112" width="180" height="154"/>
    <rect class="sheet" x="90" y="120" width="66" height="138"/>
    <use href="#articleRules" x="90" y="120"/>
    <rect class="swatch" x="171" y="121" width="66" height="58"/>
  </g>

  <!-- Stage 2: text article with annotation -->
  <g class="stage">
    <text class="stage-label" x="302" y="70">A text article with</text>
    <text class="stage-label" x="302" y="96">annotation data</text>
    <rect class="panel" x="302" y="112" width="181" height="154"/>
    <rect class="sheet" x="318" y="120" width="68" height="138"/>
    <use href="#articleRules" x="319" y="120"/>
    <rect class="sheet" x="404" y="122" width="66" height="58"/>
    <text class="annotation-bits" x="408" y="132">1010 10 11 0010</text>
    <text class="annotation-bits" x="408" y="142">1110011 0011 01</text>
    <text class="annotation-bits" x="408" y="152">0010 1101001 11</text>
    <text class="annotation-bits" x="408" y="162">10001</text>
  </g>

  <!-- Stage 3: paragraph-size texteme -->
  <g class="stage">
    <text class="stage-label" x="524" y="110">A parahraph-size</text>
    <text class="stage-label" x="524" y="136">texteme with</text>
    <text class="stage-label" x="524" y="163">annotation data</text>
    <rect class="panel" x="524" y="181" width="180" height="85"/>
    <rect class="sheet" x="538" y="190" width="66" height="66"/>
    <line class="sheet-rule" x1="548" y1="198" x2="596" y2="198"/>
    <line class="sheet-rule" x1="558" y1="207" x2="596" y2="207"/>
    <line class="sheet-rule" x1="552" y1="216" x2="596" y2="216"/>
    <line class="sheet-rule" x1="546" y1="225" x2="596" y2="225"/>
    <line class="sheet-rule" x1="556" y1="234" x2="596" y2="234"/>
    <line class="sheet-rule" x1="550" y1="243" x2="596" y2="243"/>
    <rect class="sheet" x="626" y="190" width="66" height="44"/>
    <text class="annotation-bits" x="630" y="201">101010 110010</text>
    <text class="annotation-bits" x="630" y="211">1110011 00101</text>
    <text class="annotation-bits" x="630" y="221">00110010 11010</text>
  </g>

  <!-- Stage 4: sentence-size micro-texteme -->
  <g class="stage">
    <text class="stage-label" x="750" y="133">A sentenced-size</text>
    <text class="stage-label" x="750" y="159">micro-texteme with</text>
    <text class="stage-label" x="750" y="185">annotation data</text>
    <rect class="panel" x="750" y="202" width="180" height="64"/>
    <rect class="sheet" x="762" y="212" width="64" height="18"/>
    <line class="sheet-rule" x1="768" y1="221" x2="820" y2="221"/>
    <rect class="sheet" x="850" y="212" width="67" height="44"/>
    <text class="annotation-bits" x="854" y="223">101010 110010</text>
    <text class="annotation-bits" x="854" y="233">1110011</text>
    <text class="annotation-bits" x="854" y="243">0011001</text>
  </g>

  <!-- Stage 5: structured statement -->
  <g class="stage">
    <text class="stage-label" x="974" y="160">A structured statement</text>
    <text class="stage-label" x="974" y="187">with no text</text>
    <rect class="panel" x="974" y="202" width="181" height="64"/>
    <rect class="statement-bar" x="990" y="212" width="66" height="18"/>
    <rect class="sheet" x="1074" y="212" width="66" height="44"/>
    <text class="annotation-bits" x="1078" y="223">101010 110010</text>
    <text class="annotation-bits" x="1078" y="233">1110011 00101</text>
    <text class="annotation-bits" x="1078" y="243">00110010 11010</text>
  </g>

  <!-- Axis -->
  <g class="axis">
    <path d="M70 316 H1100 V308 L1152 322 L1100 336 V328 H70 Z" fill="url(#axisFill)"/>
    <text class="axis-caption" x="613" y="366" text-anchor="middle">Decreasing language \ Increasing structure</text>
  </g>
</svg>
</body>
</html>
```